Trivia Game

I need a website designed for a Wordpress site. The site will be a contest site that will allow players to compete in trivia contests for money, including crypto currencies.

Target Market(s)

people who want to play trivia games for cash

Industry/Entity Type

Games

Number of Pages Required

1 page

Colors

Designer to choose colors to be used in the design.

Requirements
Must have
• A place for a video. A call to action - Signup.
• Black and gold like a casino.
• Very classy
Nice to have
• attached are some examples of the style I want. Very sparkly, clean classy, like a casino.

```html
<!DOCTYPE html>
<html lang="en">
<head>
<meta charset="utf-8">
<title>Aurelo — Play Online Trivia Contests</title>
<link rel="stylesheet" href="https://fonts.googleapis.com/css2?family=Oswald:wght@500;600&family=Lato:ital,wght@0,400;0,700;0,900;1,400&display=swap">
<style>
:root{
  --gold:#c9a040;
  --gold-light:#d8b152;
  --gold-dark:#a87e2a;
  --black:#0f0f0f;
  --ink:#1a1a1a;
  --panel:#2a2a2a;
  --dark:#1b1b1b;
  --header:#2d2d2d;
  --text:#e4e4e4;
  --muted:#cfcfcf;
  --white:#ffffff;
}
*{margin:0;padding:0;box-sizing:border-box}
html,body{width:1200px;height:2222px;overflow:hidden;background:var(--ink)}
body{position:relative;font-family:"Lato",sans-serif;color:var(--text)}
.abs{position:absolute}
a{color:inherit;text-decoration:none}

/* header */
.site-header{position:absolute;left:0;top:0;width:1200px;height:112px;background:var(--header);border-bottom:2px solid var(--gold-dark)}
.brand{left:74px;top:22px;font-family:"Oswald",sans-serif;font-weight:600;font-size:56px;line-height:1;color:var(--gold);letter-spacing:1px}
.search{left:732px;top:22px;width:203px;height:30px;border-bottom:1px solid #8a8a8a;font-size:14px;color:#bdbdbd;padding:4px 2px}
.search svg{position:absolute;right:4px;top:6px}
.btn-outline,.btn-gold-sm{top:18px;height:33px;font-size:13px;font-weight:700;display:flex;align-items:center;justify-content:center;letter-spacing:.5px}
.btn-outline{left:944px;width:85px;border:2px solid var(--white);color:var(--white)}
.btn-gold-sm{left:1040px;width:85px;background:var(--gold);color:var(--white)}
.main-nav{top:76px;left:0;width:1200px}
.main-nav a{position:absolute;white-space:nowrap;font-size:13px;font-weight:700;color:var(--white);letter-spacing:.3px}
.main-nav a.active{color:var(--gold)}

/* hero */
.hero{left:75px;top:136px;width:1051px;height:535px;border:5px solid var(--gold-light);outline:2px solid #f1e3c0;outline-offset:-8px;background:linear-gradient(100deg,#6b6d70 0%,#8c8f93 35%,#2c7d86 62%,#1c5e68 100%)}
.hero-title{left:0;top:222px;width:1041px;text-align:center;font-family:"Oswald",sans-serif;font-weight:600;font-size:42px;line-height:48px;letter-spacing:-.8px;color:var(--white);text-shadow:0 2px 6px rgba(0,0,0,.6)}
.hero-title em{font-style:normal;color:var(--gold-light)}
.btn-black{left:450px;top:330px;width:150px;height:34px;background:var(--black);color:var(--white);font-size:15px;font-weight:700;display:flex;align-items:center;justify-content:center}
.dots{display:flex;gap:8px}
.dots span{width:11px;height:11px;border-radius:50%;background:var(--white)}
.dots span:first-child{background:var(--gold)}
.hero .dots{position:absolute;left:489px;top:486px}

/* sections */
.section{position:absolute;left:0;width:1200px}
.s-welcome{top:673px;height:279px;background:var(--dark)}
.s-how{top:952px;height:366px;background:var(--panel)}
.s-what{top:1318px;height:363px;background:#171717}
.s-reviews{top:1681px;height:367px;background:#2b2b2b}
.site-footer{top:2048px;height:174px;background:#141414}

.h2{font-size:25px;font-weight:700;color:var(--white);letter-spacing:.5px}
.copy{font-size:14px;line-height:23px;color:var(--muted)}
.btn-gold{height:34px;background:var(--gold);color:var(--white);font-size:14.5px;font-weight:700;display:flex;align-items:center;justify-content:center}

.signup{left:703px;top:44px;width:423px;height:187px;background:linear-gradient(135deg,#d4ab4d 0%,#b98c34 55%,#a67a26 100%);padding:18px 22px}
.signup p{font-size:14.5px;line-height:22px;color:#fbf3df;margin-top:4px;width:362px}
.signup .field{position:absolute;left:22px;top:114px;width:280px;height:46px;background:var(--white);color:#6d6d6d;font-size:13.5px;padding:14px 12px}
.signup .go{position:absolute;left:311px;top:114px;width:90px;height:46px;background:var(--black);color:var(--white);font-size:14px;font-weight:700;display:flex;align-items:center;justify-content:center}

.media{background:linear-gradient(120deg,#d8a055,#e9c98a 50%,#c88b3e)}
.play{position:absolute;left:224px;top:107px}

.review{width:330px}
.stars{display:flex;gap:4px}
.review q{display:block;margin-top:14px;font-style:italic;font-size:14px;line-height:23px;color:var(--muted);quotes:"\201C\00a0" "\201D"}
.review .name{margin-top:22px;font-size:15px;color:var(--gold)}

.foot-nav a{position:absolute;white-space:nowrap;font-size:13px;font-weight:700;color:var(--white)}
.legal{left:0;top:76px;width:1200px;text-align:center;font-size:13px;color:#cfcfcf}
.social{left:502px;top:110px;display:flex;gap:23px}
.social span{width:20px;height:20px;border:2px solid var(--white);border-radius:3px}
</style>
</head>
<body>

<header class="site-header">
  <div class="abs brand">AURELO</div>
  <div class="abs search">Search..
    <svg width="16" height="16" viewBox="0 0 16 16"><circle cx="6.5" cy="6.5" r="5" fill="none" stroke="#fff" stroke-width="2"/><line x1="10.2" y1="10.2" x2="15" y2="15" stroke="#fff" stroke-width="2.2"/></svg>
  </div>
  <a class="abs btn-outline">LOG IN</a>
  <a class="abs btn-gold-sm">SIGN IN</a>
  <nav class="abs main-nav">
    <a class="active" style="left:385px">HOME</a>
    <a style="left:468px">ABOUT US</a>
    <a style="left:577px">TRIVIA CONTESTS</a>
    <a style="left:734px">BLOG</a>
    <a style="left:811px">REVIEWS</a>
    <a style="left:913px">LATEST NEWS</a>
    <a style="left:1043px">CONTACT US</a>
  </nav>
</header>

<section class="abs hero" role="img" aria-label="Man playing a trivia game on a computer monitor">
  <h1 class="abs hero-title">PLAY ONLINE <em>TRIVIA CONTEST</em> AND CHANCE TO<br>WIN <em>MONEY &amp; CRYPTO CURRENCIES</em></h1>
  <a class="abs btn-black">SIGN UP TODAY</a>
  <div class="dots"><span></span><span></span><span></span><span></span></div>
</section>

<section class="section s-welcome">
  <h2 class="abs h2" style="left:76px;top:37px">WELCOME TO AURELO</h2>
  <p class="abs copy" style="left:75px;top:84px;width:590px">Aliquam molestie, mi et imperdiet euismod, dui purus auctor tellus, et interdum lacus lectus et ante. Sed accumsan sollicitudin sapien, sit amet adipiscing turpis gravida ac.<br>In congue, neque ac lobortis volutpat, libero mauris varius mi, vitae suscipit ipsum ligula vitae risus.</p>
  <a class="abs btn-gold" style="left:75px;top:197px;width:106px">Read More</a>
  <div class="abs signup">
    <h2 class="h2">QUICK SIGNUP</h2>
    <p>Aliquam molestie, mi et imperdiet euismod, dui purus auctor tellus aliquam nibh..</p>
    <div class="field">Enter Email Address</div>
    <a class="go">SIGN UP</a>
  </div>
</section>

<section class="section s-how">
  <div class="abs media" style="left:75px;top:45px;width:512px;height:276px" role="img" aria-label="Video: smiling woman holding cash with gold coins behind her">
    <svg class="play" width="64" height="64" viewBox="0 0 64 64"><circle cx="32" cy="32" r="31" fill="#fff"/><path d="M25 19 L47 32 L25 45 Z" fill="#c9a040"/></svg>
  </div>
  <h2 class="abs h2" style="left:628px;top:81px">HOW IT WORKS</h2>
  <p class="abs copy" style="left:627px;top:128px;width:495px">Aliquam molestie, mi et imperdiet euismod, dui purus auctor tellus, et interdum lacus lectus et ante. Sed accumsan sollicitudin sapien, sit amet adipiscing turpis gravida ac. In congue, neque ac lobortis volutpat, libero mauris varius mi, vitae suscipit ipsum ligula vitae risus.</p>
  <a class="abs btn-gold" style="left:627px;top:234px;width:142px">Watch A Video</a>
</section>

<section class="section s-what">
  <h2 class="abs h2" style="left:76px;top:79px">WHAT WE DO</h2>
  <p class="abs copy" style="left:75px;top:125px;width:495px">Aliquam molestie, mi et imperdiet euismod, dui purus auctor tellus, et interdum lacus lectus et ante. Sed accumsan sollicitudin sapien, sit amet adipiscing turpis gravida ac. In congue, neque ac lobortis volutpat, libero mauris varius mi, vitae suscipit ipsum ligula vitae risus.</p>
  <a class="abs btn-gold" style="left:75px;top:239px;width:106px">Read More</a>
  <div class="abs" style="left:615px;top:44px;width:511px;height:275px;background:linear-gradient(120deg,#1d3550,#2b4a6a 40%,#1a1a22 70%,#3a2a3a)" role="img" aria-label="Gamer with headset playing at a computer in a gaming room"></div>
</section>

<section class="section s-reviews">
  <svg width="0" height="0" style="position:absolute"><defs><path id="st" d="M8 0l2.4 5 5.4.6-4 3.7 1.1 5.4L8 12 3.1 14.7l1.1-5.4-4-3.7 5.4-.6z"/></defs></svg>
  <h2 class="abs h2" style="left:0;top:44px;width:1200px;text-align:center">REVIEWS</h2>
  <div class="abs review" style="left:75px;top:100px">
    <div class="stars"><svg width="80" height="16" viewBox="0 0 80 16"><g fill="#e8992a"><use href="#st"/><use href="#st" x="16"/><use href="#st" x="32"/><use href="#st" x="48"/><use href="#st" x="64"/></g></svg></div>
    <q>Aliquam molestie, mi et imperdiet euismod, dui purus auctor tellus, et interdum lacus lectus et ante. Sed accumsan sollicitudin sapien, sit amet adipiscing turpis gravida ac...</q>
    <div class="name">-Name Heading</div>
  </div>
  <div class="abs review" style="left:435px;top:100px">
    <div class="stars"><svg width="80" height="16" viewBox="0 0 80 16"><g fill="#e8992a"><use href="#st"/><use href="#st" x="16"/><use href="#st" x="32"/><use href="#st" x="48"/><use href="#st" x="64"/></g></svg></div>
    <q>Aliquam molestie, mi et imperdiet euismod, dui purus auctor tellus, et interdum lacus lectus et ante. Sed accumsan sollicitudin sapien, sit amet adipiscing turpis gravida ac...</q>
    <div class="name">-Name Heading</div>
  </div>
  <div class="abs review" style="left:795px;top:100px">
    <div class="stars"><svg width="80" height="16" viewBox="0 0 80 16"><g fill="#e8992a"><use href="#st"/><use href="#st" x="16"/><use href="#st" x="32"/><use href="#st" x="48"/><use href="#st" x="64"/></g></svg></div>
    <q>Aliquam molestie, mi et imperdiet euismod, dui purus auctor tellus, et interdum lacus lectus et ante. Sed accumsan sollicitudin sapien, sit amet adipiscing turpis gravida ac...</q>
    <div class="name">-Name Heading</div>
  </div>
  <div class="abs dots" style="left:571px;top:309px"><span></span><span></span><span></span><span></span></div>
</section>

<footer class="section site-footer">
  <nav class="foot-nav">
    <a style="left:229px;top:44px">HOME</a>
    <a style="left:312px;top:44px">ABOUT US</a>
    <a style="left:421px;top:44px">TRIVIA CONTESTS</a>
    <a style="left:578px;top:44px">BLOG</a>
    <a style="left:656px;top:44px">REVIEWS</a>
    <a style="left:757px;top:44px">LATEST NEWS</a>
    <a style="left:888px;top:44px">CONTACT US</a>
  </nav>
  <p class="abs legal">Copyright © 2018. Company Name. All Right Reserved</p>
  <div class="abs social" aria-label="Social links"><span></span><span></span><span></span><span></span><span></span></div>
</footer>

</body>
</html>
```